I am looking for business cards and letterhead

I want a high-level look for CEO's who want a concierge level leadership consultant and organization development strategist

This needs to go with my brand: simple, elegant, clean. Please improve on this design while using these fonts and colors

Here is my website: CorinneHalvers.com

```html
<!DOCTYPE html>
<html lang="en">
<head>
<meta charset="utf-8">
<title>Corinne Halvers – Business Card &amp; Letterhead</title>
<link href="https://fonts.googleapis.com/css2?family=Poppins:wght@400;500;600;700&family=Source+Sans+3:wght@400;600;700&display=swap" rel="stylesheet">
<style>
:root{
  --bg:#d5dadc;
  --paper:#ffffff;
  --navy:#1b1b26;
  --blue:#1a5cb8;
  --gold:#e5c285;
  --ink:#111111;
  --white:#ffffff;
  --pattern:#22222c;
}
*{margin:0;padding:0;box-sizing:border-box}
html,body{width:1200px;height:983px;overflow:hidden}
body{background:var(--bg);position:relative;font-family:"Source Sans 3",sans-serif;color:var(--ink)}

/* ---------- Business card ---------- */
.card{position:absolute;left:85px;width:377px;height:215px;border-radius:22px;border:2px solid var(--gold);overflow:hidden;background:var(--navy);font-family:"Poppins",sans-serif}
.card--front{top:463px}
.card--back{top:700px}
.card__pattern{position:absolute;inset:0;background:radial-gradient(circle at 50% 50%,#2a2a35 0,var(--pattern) 70%)}
.brand-seal{position:absolute;border-radius:50%;border:3px double var(--gold);display:flex;align-items:center;justify-content:center;text-align:center;background:var(--navy)}
.brand-seal__name{font-family:"Poppins",sans-serif;font-weight:600;color:var(--blue);line-height:1.15}
.card--front .brand-seal{left:135px;top:54px;width:104px;height:104px}
.card--front .brand-seal__name{font-size:13px}
.card__site{position:absolute;left:0;right:0;top:184px;text-align:center;font-size:10px;color:var(--white)}
.hl{color:var(--blue)}
.card--back .brand-seal{left:34px;top:46px;width:118px;height:118px}
.card--back .brand-seal__name{font-size:14px}
.card__divider{position:absolute;left:186px;top:36px;width:1.5px;height:143px;background:var(--blue)}
.card__details{position:absolute;left:216px;top:50px;color:var(--white)}
.card__name{font-size:16.5px;font-weight:500;line-height:1;letter-spacing:.2px}
.card__name .first{color:var(--blue);font-weight:600}
.card__name .last{color:var(--gold)}
.card__title{font-size:8.5px;font-weight:500;margin-top:3px}
.card__address{font-size:8.5px;line-height:12.5px;margin-top:8px}
.card__contacts{list-style:none;font-size:9px;line-height:12.5px;margin-top:8px}
.card__contacts li{display:flex;align-items:center;gap:6px}
.card__contacts svg{width:8px;height:8px;flex:none}
.card__footer{position:absolute;left:0;bottom:0;width:377px;height:30px}
.card__follow{position:absolute;left:236px;bottom:3px;font-size:9.5px;color:var(--white)}

/* ---------- Letterhead ---------- */
.letterhead{position:absolute;left:506px;top:71px;width:598px;height:844px;background:var(--paper);overflow:hidden}
.letterhead .brand-seal{left:29px;top:31px;width:86px;height:86px;background:var(--paper);border-width:3px}
.letterhead .brand-seal__name{font-size:11px}
.lh-contacts{position:absolute;right:31px;top:27px;list-style:none;font-family:"Poppins",sans-serif;font-size:13px;line-height:16.4px;text-align:right}
.lh-contacts li{display:flex;justify-content:flex-end;align-items:center;gap:7px}
.lh-contacts svg{width:11px;height:11px}
.lh-watermark{position:absolute;left:117px;top:283px;width:368px;height:368px;border-radius:50%;border:10px double rgba(229,194,133,.12)}
.lh-body{position:absolute;left:33px;top:202px;width:534px}
.lh-date{font-size:11.5px}
.lh-recipient{margin-top:14px}
.lh-recipient__name{font-family:"Open Sans","Source Sans 3",sans-serif;font-weight:700;font-size:15px;line-height:1}
.lh-recipient__role{font-size:11.5px;line-height:14px}
.lh-recipient__address{font-size:11.5px;line-height:15px;margin-top:8px}
.lh-salutation{font-weight:700;font-size:15px;margin-top:26px}
.lh-text{font-size:12.2px;line-height:15.7px;text-align:justify;margin-top:10px}
.lh-text + .lh-text{margin-top:15.5px}
.lh-signature{width:161px;height:36px;margin-top:35px;background:linear-gradient(90deg,#f3f3f3,#e6e6e6)}
.lh-signer{font-family:"Open Sans","Source Sans 3",sans-serif;font-weight:700;font-size:27px;line-height:1;margin-top:2px}
.lh-signer__role{font-size:11.5px;margin-top:2px}
.lh-footer{position:absolute;left:0;bottom:0;width:598px;height:40px}
.lh-footer__address{position:absolute;right:36px;bottom:7px;font-family:"Poppins",sans-serif;font-size:12.5px;color:var(--white);display:flex;align-items:center;gap:8px}
.lh-footer__address svg{width:11px;height:13px}
</style>
</head>
<body>

<section class="card card--front" aria-label="Business card front">
  <div class="card__pattern" role="img" aria-label="Dark embossed repeating seal pattern"></div>
  <div class="brand-seal"><span class="brand-seal__name">Corinne<br>Halvers</span></div>
  <p class="card__site">www.<span class="hl">CorinneHalvers</span>.com</p>
</section>

<section class="card card--back" aria-label="Business card back">
  <div class="brand-seal"><span class="brand-seal__name">Corinne<br>Halvers</span></div>
  <div class="card__divider"></div>
  <div class="card__details">
    <h2 class="card__name"><span class="first">Corinne</span> <span class="last">Halvers</span></h2>
    <p class="card__title">Founder &amp; CEO</p>
    <p class="card__address">1840 Linden Ave. Suite 310<br>Brookfield, TX 75099</p>
    <ul class="card__contacts">
      <li><svg viewBox="0 0 10 10"><path d="M2 1l2 2-1 1c.5 1.2 1.8 2.5 3 3l1-1 2 2-1.5 1.5C4.5 9 1 5.5.5 2.5z" fill="var(--blue)"/></svg>(555) 214-0387</li>
      <li><svg viewBox="0 0 10 10"><circle cx="5" cy="5" r="4.3" fill="none" stroke="var(--blue)" stroke-width="1.2"/><path d="M.7 5h8.6M5 .7c-2 2.5-2 6 0 8.6M5 .7c2 2.5 2 6 0 8.6" stroke="var(--blue)" stroke-width=".8" fill="none"/></svg>www.<span class="hl">CorinneHalvers</span>.com</li>
      <li><svg viewBox="0 0 10 10"><rect x=".7" y="2" width="8.6" height="6.5" fill="none" stroke="var(--blue)" stroke-width="1.1"/><path d="M.7 2L5 5.5 9.3 2" stroke="var(--blue)" fill="none"/></svg>info@<span class="hl">CorinneHalvers</span>.com</li>
    </ul>
  </div>
  <svg class="card__footer" viewBox="0 0 377 30" preserveAspectRatio="none">
    <path d="M0 30C60 18 150 8 260 6L377 6V30Z" fill="var(--gold)"/>
    <path d="M50 30C120 18 200 9 265 9L377 9V30Z" fill="var(--blue)"/>
  </svg>
  <p class="card__follow">Follow us</p>
</section>

<section class="letterhead" aria-label="A4 letterhead">
  <div class="lh-watermark"></div>
  <div class="brand-seal"><span class="brand-seal__name">Corinne<br>Halvers</span></div>
  <ul class="lh-contacts">
    <li>(555) 214-0387 <svg viewBox="0 0 10 10"><path d="M2 1l2 2-1 1c.5 1.2 1.8 2.5 3 3l1-1 2 2-1.5 1.5C4.5 9 1 5.5.5 2.5z" fill="var(--blue)"/></svg></li>
    <li><span>www.<span class="hl">CorinneHalvers</span>.com</span> <svg viewBox="0 0 10 10"><circle cx="5" cy="5" r="4.3" fill="none" stroke="var(--blue)" stroke-width="1.2"/><path d="M.7 5h8.6M5 .7c-2 2.5-2 6 0 8.6M5 .7c2 2.5 2 6 0 8.6" stroke="var(--blue)" stroke-width=".8" fill="none"/></svg></li>
    <li><span>info@<span class="hl">CorinneHalvers</span>.com</span> <svg viewBox="0 0 10 10"><rect x=".7" y="2" width="8.6" height="6.5" fill="none" stroke="var(--blue)" stroke-width="1.1"/><path d="M.7 2L5 5.5 9.3 2" stroke="var(--blue)" fill="none"/></svg></li>
  </ul>

  <div class="lh-body">
    <p class="lh-date">August-05-2019</p>
    <div class="lh-recipient">
      <p class="lh-recipient__name">Helena Varga</p>
      <p class="lh-recipient__role">Director</p>
      <p class="lh-recipient__address">1840 Linden Ave. Suite 310<br>Brookfield, TX 75099</p>
    </div>
    <p class="lh-salutation">Helena Varga</p>
    <p class="lh-text">Lorem ipsum dolor sit amet, consectetuer adipiscing elit, sed diam nonummy nibh euismod tincidunt ut laoreet dolore magna aliquam erat volutpat. Ut wisi enim ad minim veniam, quis nostrud exerci tation ullamcorper suscipit lobortis</p>
    <p class="lh-text">Lorem ipsum dolor sit amet, cons ectetuer adipiscing elit, sed diam nonummy nibh euismod tincidunt ut laoreet dolore magna aliquam erat volutpat. Ut wisi enim ad minim veniam, quis nostrud exerci tation ullamcorper suscipit lobortis nisl ut aliquip ex ea commodo consequat. Lorem ipsum dolor sit amet, consectetuer olutpat. Ut wisi enim ad minim veniam, quis nostrud exerci tation ullamcorper suscipit lobortis nisl ut aliquip ex ea commodo consequat. Duis autem</p>
    <p class="lh-text">vel eum iriure dolor in hendrerit in vulputate velit esse molestie consequat, vel illum dolore eu feugiat nulla facilisis at vero eros et accumsan et iusto odio dignissim qui blandit praesent luptatum zzril delenit augue duis dolore te feugait nulla facilisi. Lorem ipsum dolor sit amet, cons ectetuer adipiscing elit, sed diam nonummy nibh euismod tincidunt ut laoreet dolore magna aliquam erat volutpat. Ut wisi enim .</p>
    <div class="lh-signature" role="img" aria-label="Handwritten signature"></div>
    <p class="lh-signer">Jonah Pryce</p>
    <p class="lh-signer__role">Co-Founder</p>
  </div>

  <svg class="lh-footer" viewBox="0 0 598 40" preserveAspectRatio="none">
    <path d="M0 40C120 20 270 6 425 4L598 4V40Z" fill="var(--gold)"/>
    <path d="M125 40C230 22 340 6 440 6L598 6V40Z" fill="var(--blue)"/>
  </svg>
  <p class="lh-footer__address">1840 Linden Ave. Suite 310, Brookfield, TX 75099
    <svg viewBox="0 0 11 13"><path d="M5.5 12S1 7.5 1 4.8a4.5 4.5 0 019 0C10 7.5 5.5 12 5.5 12z" fill="none" stroke="var(--white)" stroke-width="1.3"/><circle cx="5.5" cy="4.8" r="1.5" fill="var(--white)"/></svg>
  </p>
</section>

</body>
</html>
```